Web Design Project

Psychotherapy and Counselling Practice needs a landing page web design.

My business "Harbourlight Consulting" specialises in the treatment of Anxiety and Depression with a holistic approach, endeavouring to unlock the key that holds us to ransom in a life that is imbalanced, frustrating, and ultimately of our own making due to our own perceptions and behaviours.

There is much that impacts us which we cannot change, but we are always in control of how we think, and how we frame our experiences.....learning to challenge those thoughts and behaviours that are destructive and disempowering opens up a world of joyful possibility. Life is about making choices, learn to make wiser and healthier choices.......

Harbourlight Consulting has a client base of individual clients but will seek to expand to offer services to the Corporate world by offering an adjunct to employers for established "Wellness Programs".

Harbourlight Consulting is a highly professional, ethically bound business, with the needs of the client at the forefront of all we do.

Harbourlight Consulting wishes to avoid the usual "jargon driven" psychobabble offered on many counselling web pages. It aims to be stylishly presented, clean in look and with as few "words" as possible and a largely white background (faster loading and more powerful impact of what is stated), those words contained in the webpage should be meaningful, persuasive and have an impact simply at glance. Harbourlight does not want , or expect, those prospective clients in need of support , to be reading through volumes of industry driven cliches.

At this point Harbourlight is just looking for a high quality landing page. However in time this will likely expand to include other sections such as case studies, video content etc.

Target Market(s)

Those in need of emotional support, suffering mental health issues, and those simply wanting to become self aware supported by a mindful therapist.

Industry/Entity Type

Industry

Requirements
Must have
• The design must incorporate the Harbourlight logo and colour schemes found on the attached files.

```html
<!DOCTYPE html>
<html lang="en">
<head>
<meta charset="utf-8">
<title>Harbourlight Consulting</title>
<link href="https://fonts.googleapis.com/css2?family=Ubuntu:ital,wght@0,300;0,400;0,500;0,700;1,400&display=swap" rel="stylesheet">
<style>
  :root {
    --green: #8cab0b;
    --green-text: #89ad10;
    --ink: #111111;
    --body: #3a3a3a;
    --quote: #333333;
    --footer: #5e5e5e;
    --footer-text: #f1f1f1;
    --page: #ffffff;
    --page-fade: #f3f2f2;
  }
  * { margin: 0; padding: 0; box-sizing: border-box; }
  html, body { width: 1200px; height: 1191px; overflow: hidden; }
  body {
    font-family: "Ubuntu", sans-serif;
    background: linear-gradient(to bottom, var(--page) 0, var(--page) 540px, var(--page-fade) 1037px);
    position: relative;
    color: var(--body);
  }
  .hero-band {
    position: absolute; left: 0; top: 233px; width: 1200px; height: 267px;
    background: var(--green);
  }
  .hero-photo {
    position: absolute; left: 240px; top: 56px; width: 351px; height: 444px;
    border-radius: 150px 150px 0 0;
    background: linear-gradient(to bottom, #e7c6a6 0%, #f2e2d3 35%, #fafafa 60%, #c8e07a 78%, #f4f4f4 100%);
  }
  .brand-name {
    position: absolute; left: 696px; top: 112px;
    font-size: 38px; font-weight: 300; letter-spacing: 1px;
    color: var(--green-text);
  }
  .hero-copy { position: absolute; left: 696px; top: 283px; width: 360px; color: #fff; }
  .hero-copy h1 { font-size: 23px; font-weight: 700; line-height: 23px; }
  .hero-copy p { margin-top: 12px; font-size: 15.5px; font-weight: 500; line-height: 22px; }
  .cta {
    position: absolute; left: 699px; top: 413px; width: 201px; height: 46px;
    border-radius: 4px; background: linear-gradient(#fafafa, #dcdcdc);
    box-shadow: 0 1px 2px rgba(0,0,0,.3);
    display: flex; align-items: center;
  }
  .cta-icon { width: 50px; height: 100%; border-right: 1px solid #c4c4c4; display: flex; align-items: center; justify-content: center; }
  .cta-label { padding-left: 9px; font-size: 12px; font-weight: 700; color: #666; letter-spacing: -.2px; }
  .service { position: absolute; top: 562px; width: 240px; }
  .service h2 { display: flex; align-items: center; gap: 6px; font-size: 23px; font-weight: 400; color: var(--ink); }
  .service h3 { margin-left: 26px; font-size: 15.5px; font-weight: 400; color: var(--green-text); }
  .service p { margin-top: 8px; margin-left: 3px; font-size: 12px; line-height: 18px; }
  .divider { position: absolute; left: 206px; top: 790px; width: 823px; height: 1px; background: linear-gradient(to right, transparent, #e2e2e2 15%, #e2e2e2 85%, transparent); }
  .quote { position: absolute; left: 200px; top: 818px; width: 835px; text-align: center; font-style: italic; font-size: 15.5px; line-height: 24.5px; color: var(--quote); }
  .site-footer { position: absolute; left: 0; top: 1037px; width: 1200px; height: 154px; background: var(--footer); color: var(--footer-text); }
  .footer-nav { position: absolute; left: 205px; top: 33px; font-size: 10px; display: flex; gap: 8px; }
  .footer-nav span.sep { color: #aaa; }
  .footer-brand { position: absolute; left: 206px; top: 71px; font-size: 10px; color: #ddd; }
  .footer-brand b { font-size: 14px; font-weight: 400; color: var(--green-text); margin-right: 6px; letter-spacing: .5px; }
  .appointment { position: absolute; left: 777px; top: 30px; font-size: 12px; }
  .appointment h4 { font-size: 12px; font-weight: 500; margin-bottom: 12px; }
  .appointment div { line-height: 15px; }
  .appointment small { font-size: 9.5px; color: #ccc; }
</style>
</head>
<body>
  <div class="hero-band"></div>
  <div class="hero-photo" role="img" aria-label="Photo of a young child holding a green paper cut-out chain of people"></div>
  <div class="brand-name">HARBOURLIGHT</div>
  <section class="hero-copy">
    <h1>Specialists in the treatment<br>of Anxiety and Depression</h1>
    <p>Life is about making choices, learn to make wiser and healthier choices.</p>
  </section>
  <a class="cta">
    <span class="cta-icon"><svg width="22" height="22" viewBox="0 0 22 22"><path d="M2 7h9V2l9 9-9 9v-5H2z" fill="#555"/></svg></span>
    <span class="cta-label">REQUEST APPOINTMENT</span>
  </a>

  <article class="service" style="left:214px">
    <h2><svg width="20" height="24" viewBox="0 0 20 24"><path d="M2 23C1 12 6 4 19 1 17 12 12 18 4 19z" fill="#666"/></svg>Holistic</h2>
    <h3>Lorem ipsum dolor</h3>
    <p>In purus erat, scelerisque eget tincidunt et,tempus eget orci. Sed ullamcorper nulla vel quam blandit feugiat. Maecenas elit velit, ornare id ultricies eu, gravida ac augue.&nbsp; Fusce dignissim tincidunt magna, tempus viverra mauris egestas in. Maecenas lorem orci.</p>
  </article>
  <article class="service" style="left:511px">
    <h2><svg width="21" height="20" viewBox="0 0 21 20"><path d="M10.5 0L21 20H0z" fill="#666"/></svg>Wellness Programs</h2>
    <h3>Lorem ipsum dolor</h3>
    <p>In purus erat, scelerisque eget tincidunt et,tempus eget orci. Sed ullamcorper nulla vel quam blandit feugiat. Maecenas elit velit, ornare id ultricies eu, gravida ac augue.&nbsp; Fusce dignissim tincidunt magna, tempus viverra mauris egestas in. Maecenas lorem orci.</p>
  </article>
  <article class="service" style="left:801px">
    <h2><svg width="24" height="23" viewBox="0 0 24 23"><path d="M12 0l3 8h9l-7 5 3 9-8-6-8 6 3-9-7-5h9z" fill="#666"/></svg>Individual Therapy</h2>
    <h3>Lorem ipsum dolor</h3>
    <p>In purus erat, scelerisque eget tincidunt et,tempus eget orci. Sed ullamcorper nulla vel quam blandit feugiat. Maecenas elit velit, ornare id ultricies eu, gravida ac augue.&nbsp; Fusce dignissim tincidunt magna, tempus viverra mauris egestas in. Maecenas lorem orci.</p>
  </article>

  <div class="divider"></div>
  <blockquote class="quote">There is much that impacts us which we cannot change, but we are always in control of how we think, and how we frame our experiences. Learning to challenge those thoughts and behaviours that are destructive and disempowering opens up a world of joyful possibility. Life is about making choices, learn to make wiser and healthier choices.</blockquote>

  <footer class="site-footer">
    <nav class="footer-nav"><span>About Us</span><span class="sep">|</span><span>Case Studies</span><span class="sep">|</span><span>&nbsp;Contact</span></nav>
    <div class="footer-brand"><b>Harbourlight</b>2013 © All rights reserved</div>
    <div class="appointment">
      <h4>Appointment</h4>
      <div><small>Ph:</small> +(10) <b>555 0142 376</b></div>
      <div><small>Email:</small> info@harbourlightconsulting.com</div>
    </div>
  </footer>
</body>
</html>
```